Private label Bottled water label design

We are launching private label water bottle case packs with our brand “brightway”
Need bottle labels design as well as case pack design artwork. Bottle is 16.9oz similar to pet calvora feltmoor bottles.
It will be spring water.
Case pack will be of 24 bottles
Brightway is a chain of convenience stores in Texas
www.brightwaymarkets.example
I have attached pictures of calvora water. It would be similar packaging for single and case pack.

Target Market(s)

Male female shoppers middle aged. Take home package or single serve in cold vault

Industry/Entity Type

Water bottle retail

Colors
0054AA
0677BA
7BADD7
CADEEF
E8F1F8
59FF00
82FF00
B8FF75
E3FFCB
F4FFEA

Requirements
Must have
• Very premium look. Use the logo of brightway
Nice to have
• Elegant premium water look
Should not have
• I am open to all

```html
<!DOCTYPE html>
<html lang="en">
<head>
<meta charset="utf-8">
<title>Brightway Mountain Spring Water – Bottle Label</title>
<link href="https://fonts.googleapis.com/css2?family=Nunito:wght@800&family=Montserrat:wght@400;500&display=swap" rel="stylesheet">
<style>
  :root {
    --backdrop: #93e0ee;
    --label-white: #ffffff;
    --pattern-grey: #ececec;
    --mountain-grey: #d9d9d9;
    --mountain-light: #f3f3f3;
    --brand-ink: #3d3d3d;
    --lime: #a4d414;
    --lime-light: #c7ea5e;
    --text-dark: #2b2b2b;
    --leaf-green: #8cc63f;
  }
  * { margin: 0; padding: 0; box-sizing: border-box; }
  html, body {
    width: 934px;
    height: 1200px;
    overflow: hidden;
    background: var(--backdrop);
  }
  .canvas {
    position: relative;
    width: 934px;
    height: 1200px;
  }
  .bottle-label {
    position: absolute;
    left: 37px;
    top: 250px;
    width: 860px;
    height: 700px;
    background: var(--label-white);
    overflow: hidden;
  }
  .chevron-pattern {
    position: absolute;
    inset: 0 0 160px 0;
    background: linear-gradient(180deg, var(--pattern-grey) 0%, var(--label-white) 85%);
    opacity: 0.7;
  }
  .mountain-art {
    position: absolute;
    left: 90px;
    right: 90px;
    top: 300px;
    bottom: 0;
    background: radial-gradient(ellipse at 50% 10%, var(--mountain-light) 0%, var(--mountain-grey) 55%, var(--label-white) 100%);
    opacity: 0.85;
  }
  .brand-name {
    position: absolute;
    left: 0;
    right: 0;
    top: 190px;
    text-align: center;
    font-family: "Nunito", sans-serif;
    font-weight: 800;
    font-size: 118px;
    line-height: 1;
    letter-spacing: -3px;
    color: var(--brand-ink);
  }
  .natural-badge {
    position: absolute;
    left: 50%;
    top: 425px;
    transform: translateX(-50%);
    display: flex;
    flex-direction: column;
    align-items: center;
    gap: 6px;
  }
  .natural-badge__text {
    font-family: "Montserrat", sans-serif;
    font-size: 13px;
    letter-spacing: 2px;
    color: var(--text-dark);
  }
  .product-band {
    position: absolute;
    left: 0;
    right: 0;
    top: 518px;
    height: 88px;
    background: linear-gradient(90deg, var(--lime) 0%, var(--lime-light) 25%, var(--lime-light) 75%, var(--lime) 100%);
    display: flex;
    align-items: center;
    justify-content: center;
  }
  .product-band__name {
    font-family: "Montserrat", sans-serif;
    font-weight: 500;
    font-size: 30px;
    line-height: 1.1;
    text-align: center;
    color: var(--label-white);
  }
  .net-volume {
    position: absolute;
    left: 0;
    right: 0;
    top: 640px;
    text-align: center;
    font-family: "Montserrat", sans-serif;
    font-size: 25px;
    color: var(--text-dark);
  }
</style>
</head>
<body>
  <main class="canvas">
    <section class="bottle-label">
      <div class="chevron-pattern" role="img" aria-label="Faint grey chevron line pattern"></div>
      <div class="mountain-art" role="img" aria-label="Soft grey sketch of a mountain peak"></div>
      <h1 class="brand-name">brightway</h1>
      <div class="natural-badge">
        <svg width="44" height="54" viewBox="0 0 44 54" aria-hidden="true">
          <circle cx="22" cy="27" r="18" fill="none" stroke="var(--leaf-green)" stroke-width="3"/>
        </svg>
        <span class="natural-badge__text">NATURAL</span>
      </div>
      <div class="product-band">
        <p class="product-band__name">Mountain Spring<br>Water</p>
      </div>
      <p class="net-volume">16,9 oz</p>
    </section>
  </main>
</body>
</html>
```